Website design for staffing/workforce solutions company - Halvard Staffing Solutions

Create a launch-ready website
Halvard Staffing Solutions also known as HSS. This is a company that specializes in Staffing/Work force solutions for Healthcare/IT/Logistics/Maintenance/Construction/Manufacturing/Industrial/General Labor. HSS works with government agencies/contracts also. Use the attached logo in the build of the website. Website should be clean, modern, engaging, innovative. Website needs to speak to the professional services industry.
Halvard Staffing Solutions or HSS is a certified VOSB, SDVOSB, DBE and Minority-Owned Business.
The website needs to be compliant for government contracting.

Website needs to include the following--
Modern UI/UX Enhancements: A hero section with a strong call-to-action.
Government Contracting Compliance: Certification display and a Capability Statement download.
Advanced Careers Section: A dedicated job application portal.
Social Media & Lead Generation: Links to Profilary, Quillo, and Mingleo.
Security & Performance: Optimized for SEO, fast loading, and mobile responsiveness.
1. Modern Design Upgrades
๐Ÿ”น Upgrade UI/UX for a Professional, Trustworthy Look
โœ… Full-width hero banner with a high-quality background image representing business, technology, and workforce solutions.
โœ… Animated elements (subtle transitions for smooth browsing experience).
โœ… Bold CTA buttons for easy navigation to key actions (e.g., โ€œGet Startedโ€ or โ€œRequest a Consultationโ€).
โœ… Dark-themed header with contrasting colors (professional & government-trustworthy).
โœ… New Homepage Hero Section Example:
"Your Trusted Partner in Workforce, IT, Maintenance & Logistics Solutions"
Button: "Discover Our Services"

2. Enhanced Government Contracting Section (Key for Compliance)
๐Ÿ“Œ Essential for securing contracts & building credibility
โœ… Capability Statement (Downloadable PDF)

Showcase key past contracts, company qualifications, and services in a downloadable format for government buyers.
โœ… Certifications Display (VOSB, SDVOSB, DBE, Minority-Owned Business)

Visual badge display to emphasize legitimacy for government contracts.
โœ… Procurement Readiness Details

NAICS Codes, DUNS Number, CAGE Code, and relevant VPR.example registration details.
โœ… Past Performance Showcase (Case Studies Section)

Highlight successful projects and government contracts.
โœ… Compliance & Security

Add SOC 2, HIPAA (for healthcare staffing), and ITAR compliance if applicable.
3. Advanced Job Search & Candidate Portal (For Staffing Services)
๐Ÿ“Œ To attract top talent for staffing contracts

โœ… Advanced Job Search Feature

Filters: Industry, location, job type (contract/full-time), salary range, and clearance level (for government jobs).
โœ… Candidate Login Portal

Applicants can upload resumes, track applications, and receive job alerts.
โœ… Employer Portal (For Businesses Hiring Through HSS)

A dedicated section for companies to submit staffing requests and view candidate matches.
4. Service-Specific Landing Pages (SEO & Engagement)
๐Ÿ“Œ Helps different industries find relevant services faster

๐Ÿ”น Dedicated Pages for Each Service:
โœ… Staffing & Workforce Solutions

Specialized sections for Healthcare, IT, Construction, Industrial, and General Labor staffing.
โœ… IT Services

List services like Cybersecurity, Cloud Solutions, and IT Consulting.
Showcase tech stack & certifications.
โœ… Logistics & Maintenance

Detail fleet management, supply chain services, and industrial maintenance.
โœ… Government Contracting Solutions

A streamlined page for government agencies.
5. Security & Compliance Upgrades (For Government Work)
๐Ÿ“Œ To ensure compliance & credibility in government contracting

โœ… SSL Certification (100% Required for Security)

Secure client and job applicant data.
โœ… ADA Compliance (Accessibility)

Ensure the website follows WCAG 2.1 accessibility standards for government clients.
โœ… GDPR & Data Protection Features

A privacy policy and terms of service to comply with data regulations.
6. Performance & Mobile Optimization
๐Ÿ“Œ To ensure fast loading & responsiveness

โœ… Mobile-Responsive Design

Optimized for mobile-friendly navigation since many users browse from phones.
โœ… Fast-Loading Pages

Optimize images & implement lazy loading for better site speed.
โœ… SEO-Optimized Pages

Improve search ranking on Searvo with:
Keyword-optimized content (e.g., โ€œGovernment Contracting Staffing Servicesโ€)
Schema markup for job listings
Blog/articles about staffing trends
7. Social Media & Lead Generation
๐Ÿ“Œ For brand credibility & client engagement

โœ… Profilary, Quillo, Mingleo Integration

Display recent updates from Profilary (primary for B2B & government).
โœ… Lead Capture Forms

Forms for business inquiries, talent applications, and government RFPs.
โœ… Client & Candidate Testimonials
Showcase client success stories & employee experiences

Good websites to pull examples for inspiration/direction--
https://www.pelmora.example/
https://www.tovrinex.example/
https://brambleworks.example/homepage/
https://www.quantelvetting.example/capability-statement

Staffing/Professional Services

Coded - Design and coding required

5+ page

• Website needs to include the following-- Modern UI/UX Enhancements: A hero section with a strong call-to-action. Government Contracting Compliance: Certification display and a Capability Statement download. Advanced Careers Section: A dedicated job application portal. Social Media & Lead Generation: Links to Profilary, Quillo, and Mingleo. Security & Performance: Optimized for SEO, fast loading, and mobile responsiveness. 1. Modern Design Upgrades ๐Ÿ”น Upgrade UI/UX for a Professional, Trustworthy Look โœ… Full-width hero banner with a high-quality background image representing business, technology, and workforce solutions. โœ… Animated elements (subtle transitions for smooth browsing experience). โœ… Bold CTA buttons for easy navigation to key actions (e.g., โ€œGet Startedโ€ or โ€œRequest a Consultationโ€). โœ… Dark-themed header with contrasting colors (professional & government-trustworthy). โœ… New Homepage Hero Section Example: "Your Trusted Partner in Workforce, IT, & Logistics Solutions" Button: "Discover Our Services" 2. Enhanced Government Contracting Section (Key for Compliance) ๐Ÿ“Œ Essential for securing contracts & building credibility โœ… Capability Statement (Downloadable PDF) Showcase key past contracts, company qualifications, and services in a downloadable format for government buyers. โœ… Certifications Display (VOSB, SDVOSB, DBE, Minority-Owned Business) Visual badge display to emphasize legitimacy for government contracts. โœ… Procurement Readiness Details NAICS Codes, DUNS Number, CAGE Code, and relevant VPR.example registration details. โœ… Past Performance Showcase (Case Studies Section) Highlight successful projects and government contracts. โœ… Compliance & Security Add SOC 2, HIPAA (for healthcare staffing), and ITAR compliance if applicable. 3. Advanced Job Search & Candidate Portal (For Staffing Services) ๐Ÿ“Œ To attract top talent for staffing contracts โœ… Advanced Job Search Feature Filters: Industry, location, job type (contract/full-time), salary range, and clearance level (for government jobs). โœ… Candidate Login Portal Applicants can upload resumes, track applications, and receive job alerts. โœ… Employer Portal (For Businesses Hiring Through HSS) A dedicated section for companies to submit staffing requests and view candidate matches. 4. Service-Specific Landing Pages (SEO & Engagement) ๐Ÿ“Œ Helps different industries find relevant services faster ๐Ÿ”น Dedicated Pages for Each Service: โœ… Staffing & Workforce Solutions Specialized sections for Healthcare, IT, Construction, Industrial, and General Labor staffing. โœ… IT Services List services like Cybersecurity, Cloud Solutions, and IT Consulting. Showcase tech stack & certifications. โœ… Logistics & Maintenance Detail fleet management, supply chain services, and industrial maintenance. โœ… Government Contracting Solutions A streamlined page for government agencies. 5. Security & Compliance Upgrades (For Government Work) ๐Ÿ“Œ To ensure compliance & credibility in government contracting โœ… SSL Certification (100% Required for Security) Secure client and job applicant data. โœ… ADA Compliance (Accessibility) Ensure the website follows WCAG 2.1 accessibility standards for government clients. โœ… GDPR & Data Protection Features A privacy policy and terms of service to comply with data regulations. 6. Performance & Mobile Optimization ๐Ÿ“Œ To ensure fast loading & responsiveness โœ… Mobile-Responsive Design Optimized for mobile-friendly navigation since many users browse from phones. โœ… Fast-Loading Pages Optimize images & implement lazy loading for better site speed. โœ… SEO-Optimized Pages Improve search ranking on Searvo with: Keyword-optimized content (e.g., โ€œGovernment Contracting Staffing Servicesโ€) Schema markup for job listings Blog/articles about staffing trends 7. Social Media & Lead Generation ๐Ÿ“Œ For brand credibility & client engagement โœ… Profilary, Quillo, Mingleo Integration Display recent updates from Profilary (primary for B2B & government). โœ… Lead Capture Forms Forms for business inquiries, talent applications, and government RFPs. โœ… Client & Candidate Testimonials Showcase client success stories & employee experiences Good websites to pull examples for inspiration/direction-- https://www.pelmora.example/ https://www.tovrinex.example/ https://brambleworks.example/homepage/

```html
<!DOCTYPE html>
<html lang="en">
<head>
<meta charset="utf-8">
<title>Halvard Staffing Solutions – Workforce, IT &amp; Logistics</title>
<link href="https://fonts.googleapis.com/css2?family=Poppins:wght@400;500;600;700&display=swap" rel="stylesheet">
<style>
:root{
  --red:#b5111f;
  --red-bright:#d8121f;
  --navy:#1d2b4d;
  --ink:#1b1b1b;
  --text:#555;
  --pink:#fdecef;
  --pink-line:#e59aa3;
  --grey:#ebe8e9;
  --black:#0d0d0d;
  --white:#fff;
}
*{box-sizing:border-box;margin:0;padding:0}
html,body{width:1200px;height:3403px;overflow:hidden}
body{font-family:'Poppins',sans-serif;color:var(--ink);position:relative;background:var(--white)}
a{color:inherit;text-decoration:none}

/* header */
.site-header{position:absolute;left:0;top:0;width:1200px;height:51px;background:var(--red)}
.brand{position:absolute;left:122px;top:9px;color:var(--white);font-weight:600;font-size:22px;letter-spacing:1px;line-height:32px}
.nav a{position:absolute;top:17px;color:var(--white);font-size:12px}
.nav a.active{text-decoration:underline;text-underline-offset:5px}
.btn-white{position:absolute;top:10px;height:31px;background:var(--white);color:var(--ink);font-size:12px;display:flex;align-items:center;justify-content:center}
.btn-outline{position:absolute;top:10px;height:31px;border:1px solid var(--white);color:var(--white);font-size:12px;display:flex;align-items:center;justify-content:center}

/* hero */
.hero{position:absolute;left:0;top:51px;width:1200px;height:631px;background:linear-gradient(90deg,#fdf1f2 0%,#fbe8ea 40%,#f1e1e3 60%,#dfd8da 100%);overflow:hidden}
.hero-photo{position:absolute;right:0;top:0;width:640px;height:631px;
  background:
    radial-gradient(ellipse 150px 190px at 62% 24%,rgba(176,124,96,.75) 0%,rgba(176,124,96,.35) 55%,rgba(176,124,96,0) 100%),
    radial-gradient(ellipse 260px 340px at 62% 92%,#2e4a66 0%,#35526f 55%,rgba(53,82,111,0) 100%),
    radial-gradient(ellipse 260px 300px at 90% 30%,rgba(200,205,214,.9) 0%,rgba(200,205,214,0) 100%),
    linear-gradient(90deg,rgba(251,232,234,0) 0%,rgba(232,214,218,.8) 30%,#d5cfd4 60%,#cfd2d8 100%)}
.eyebrow{position:absolute;left:122px;color:var(--red);font-size:14px;display:flex;align-items:center;gap:12px}
.eyebrow::after{content:"";width:107px;height:1px;background:var(--red)}
.hero h1{position:absolute;left:122px;font-size:44px;line-height:54px;font-weight:700;text-transform:uppercase;width:600px}
.search-box{position:absolute;left:122px;width:460px;height:97px;background:#e7e3e4}
.tab{position:absolute;top:15px;font-size:11px;font-weight:500}
.tab.on{text-decoration:underline;text-underline-offset:4px}
.field{position:absolute;top:43px;height:30px;width:148px;background:var(--white);font-size:11px;color:#666;display:flex;align-items:center;justify-content:center}
.btn-navy{position:absolute;background:var(--navy);color:var(--white);font-size:11px;display:flex;align-items:center;justify-content:center}

/* about */
.about-frame{position:absolute;left:122px;top:774px;width:387px;height:250px;border:1px solid var(--pink-line);padding:6px}
.photo{width:100%;height:100%}
.section-title{position:absolute;font-weight:500;text-transform:uppercase;color:var(--ink)}
.about-copy{position:absolute;left:620px;top:822px;width:455px;font-size:11.3px;line-height:18.6px;color:var(--text)}

/* specialties */
.specialties{position:absolute;left:0;top:1088px;width:1200px;height:557px;background:var(--pink)}
.spec-card{position:absolute;top:138px;width:224px;height:357px;border-bottom:3px solid var(--red)}
.spec-label{position:absolute;left:0;bottom:0;width:100%;height:56px;background:#2b2b2b;color:var(--white);font-size:14px;font-weight:500;display:flex;align-items:center;justify-content:space-between;padding:0 14px 0 18px}
.spec-label .go{width:24px;height:24px;border:1px solid var(--white);border-radius:50%;display:flex;align-items:center;justify-content:center}
.slide-arrow{position:absolute;width:31px;height:31px;border:1.5px solid var(--red);border-radius:50%;display:flex;align-items:center;justify-content:center}

/* testimonials */
.testimonial{position:absolute;top:1780px;width:468px;height:238px;background:var(--white);box-shadow:0 2px 10px rgba(0,0,0,.09)}
.quote-mark{position:absolute;left:22px;top:-8px;font-size:120px;line-height:120px;font-weight:700;color:#f1cdd1}
.t-copy{position:absolute;left:24px;top:72px;width:420px;font-size:12px;line-height:22.4px;color:var(--text)}
.avatar{position:absolute;left:24px;top:172px;width:50px;height:50px;border-radius:50%;background:radial-gradient(circle at 50% 35%,#e9ecf0 0%,#aab3bf 50%,#3e4a5c 100%)}
.stars{position:absolute;left:86px;top:183px;color:#f4b400;font-size:10px;letter-spacing:1px}
.role{position:absolute;left:86px;top:199px;font-size:10px;font-weight:500}

/* resources */
.resources{position:absolute;left:0;top:2083px;width:1200px;height:494px;background:var(--grey)}
.res-card{position:absolute;top:139px;width:305px}
.res-img{width:305px;height:214px;border:1px solid var(--pink-line);padding:6px}
.res-title{margin-top:9px;font-size:15px;font-weight:500;line-height:19px}
.read-more{display:inline-flex;align-items:center;gap:5px;margin-top:14px;color:var(--red);font-size:11px;font-weight:500;text-decoration:underline}

/* certifications */
.badge-box{position:absolute;top:2711px;width:177px;height:99px;border:1px solid var(--pink-line);display:flex;align-items:center;justify-content:center}

/* cta */
.cta{position:absolute;left:0;top:2873px;width:1200px;height:212px;background:linear-gradient(135deg,#e3141f 0%,#c70f1b 55%,#a50d18 100%);overflow:hidden}
.cta h2{position:absolute;left:0;top:48px;width:1200px;text-align:center;color:var(--white);font-size:36px;font-weight:500}
.cta .btn{position:absolute;left:538px;top:117px;width:123px;height:31px;background:var(--white);font-size:11px;display:flex;align-items:center;justify-content:center}

/* footer */
.site-footer{position:absolute;left:0;top:3085px;width:1200px;height:318px;background:var(--black);color:var(--white)}
.f-title{position:absolute;font-size:14px;font-weight:500;text-transform:uppercase}
.f-link{position:absolute;left:411px;font-size:11px;font-weight:500}
.social{position:absolute;top:152px;width:25px;height:25px;border:1px solid var(--red-bright)}
.contact{position:absolute;left:603px;font-size:11px;line-height:14px;display:flex;gap:8px}
.contact .ico{width:17px;height:17px;border:1px solid var(--red-bright);flex:none;display:flex;align-items:center;justify-content:center}
.f-input{position:absolute;left:866px;top:99px;width:211px;height:32px;border:1px solid #555;font-size:10px;padding-left:12px;display:flex;align-items:center}
.f-sub{position:absolute;left:866px;top:138px;width:211px;height:32px;background:var(--red-bright);font-size:10px;font-weight:500;display:flex;align-items:center;justify-content:center}
.f-rule{position:absolute;left:122px;top:250px;width:955px;height:1px;background:#555}
.f-legal{position:absolute;top:260px;font-size:10px}
</style>
</head>
<body>

<header class="site-header">
  <div class="brand">HALVARD</div>
  <nav class="nav">
    <a class="active" style="left:396px">Home</a>
    <a style="left:459px">About Us</a>
    <a style="left:539px">For Job Seekers</a>
    <a style="left:657px">Solutions</a>
    <a style="left:737px">Resources</a>
  </nav>
  <a class="btn-white" style="left:819px;width:94px">Get Started</a>
  <a class="btn-outline" style="left:921px;width:156px">Request a Consultation</a>
</header>

<section class="hero">
  <div class="hero-photo" role="img" aria-label="Smiling professional in a navy suit in front of a bright blurred office"></div>
  <p class="eyebrow" style="top:139px">WELCOME TO HALVARD STAFFING SOLUTIONS</p>
  <h1 style="top:172px">Your Trusted Partner<br>in Workforce, IT, &amp;<br>Logistics Solutions</h1>
  <div class="search-box" style="top:361px">
    <span class="tab on" style="left:25px">Find A Job</span>
    <span class="tab" style="left:108px">Find Talent</span>
    <div class="field" style="left:25px">Job Title or Keyword</div>
    <div class="field" style="left:179px">Zipcode or City</div>
    <a class="btn-navy" style="left:341px;top:43px;width:94px;height:31px">Search Jobs</a>
  </div>
</section>

<div class="about-frame"><div class="photo" role="img" aria-label="Worker in a hard hat and manager reviewing a tablet inside a warehouse" style="background:radial-gradient(ellipse 90px 110px at 45% 62%,rgba(225,190,60,.75),rgba(225,190,60,0)),radial-gradient(ellipse 90px 120px at 62% 60%,rgba(150,155,165,.85),rgba(150,155,165,0)),linear-gradient(180deg,#2f4a78 0%,#4b5f7c 40%,#7f8895 75%,#9aa0a8 100%)"></div></div>
<h2 class="section-title" style="left:620px;top:766px;font-size:37px">About Us</h2>
<p class="about-copy">Halvard Staffing Solutions (HSS) is a staffing and workforce solutions company specializing in providing talent acquisition and management services across various sectors, including Healthcare, IT, Construction, Manufacturing, Industrial, General Labor, Logistics, and Maintenance. HSS also works with government agencies and contracts. They offer a range of services, including sourcing and recruitment, onboarding, and employee lifecycle management. HSS is a certified VOSB, SDVOSB, DBE, and Minority-Owned Business.</p>
<a class="btn-navy" style="left:622px;top:973px;width:155px;height:33px">Discover Our Services</a>

<section class="specialties">
  <h2 class="section-title" style="left:0;width:1200px;text-align:center;top:52px;font-size:36px">Our Specialties</h2>
  <div class="slide-arrow" style="left:67px;top:304px"><svg width="12" height="10" viewBox="0 0 12 10"><path d="M11 5H1M5 1L1 5l4 4" fill="none" stroke="#b5111f" stroke-width="1.4"/></svg></div>
  <div class="slide-arrow" style="left:1100px;top:304px"><svg width="12" height="10" viewBox="0 0 12 10"><path d="M1 5h10M7 1l4 4-4 4" fill="none" stroke="#b5111f" stroke-width="1.4"/></svg></div>

  <div class="spec-card" style="left:122px"><div class="photo" role="img" aria-label="Two manufacturing workers in hard hats and safety vests" style="height:301px;background:radial-gradient(ellipse 130px 160px at 50% 70%,#f08a3a 0%,rgba(240,138,58,.6) 55%,rgba(240,138,58,0) 100%),linear-gradient(180deg,#c9ccd1 0%,#d8cfc6 35%,#c97a3d 100%)"></div>
    <div class="spec-label" style="font-size:16px">MANUFACTURING<span class="go"><svg width="10" height="8" viewBox="0 0 10 8"><path d="M1 4h8M6 1l3 3-3 3" fill="none" stroke="#fff"/></svg></span></div></div>
  <div class="spec-card" style="left:366px"><div class="photo" role="img" aria-label="Two industrial workers walking through a warehouse" style="height:301px;background:radial-gradient(ellipse 70px 110px at 50% 55%,rgba(110,110,112,.7),rgba(110,110,112,0)),linear-gradient(180deg,#3d5c8c 0%,#6f7f96 35%,#a8adb4 70%,#b9bcc0 100%)"></div>
    <div class="spec-label">INDUSTRIAL<span class="go"><svg width="10" height="8" viewBox="0 0 10 8"><path d="M1 4h8M6 1l3 3-3 3" fill="none" stroke="#fff"/></svg></span></div></div>
  <div class="spec-card" style="left:609px"><div class="photo" role="img" aria-label="Construction workers reviewing plans on a table" style="height:301px;background:radial-gradient(ellipse 140px 120px at 55% 45%,#f0952f 0%,rgba(240,149,47,.5) 60%,rgba(240,149,47,0) 100%),linear-gradient(180deg,#b4b7bb 0%,#c9c2b6 55%,#f4f4f4 80%,#ececec 100%)"></div>
    <div class="spec-label">CONSTRUCTION<span class="go"><svg width="10" height="8" viewBox="0 0 10 8"><path d="M1 4h8M6 1l3 3-3 3" fill="none" stroke="#fff"/></svg></span></div></div>
  <div class="spec-card" style="left:854px"><div class="photo" role="img" aria-label="Laborers holding blueprints at a building site" style="height:301px;background:radial-gradient(ellipse 90px 110px at 60% 70%,rgba(232,228,222,.95),rgba(232,228,222,0)),radial-gradient(ellipse 80px 100px at 18% 75%,rgba(226,110,40,.8),rgba(226,110,40,0)),linear-gradient(180deg,#7aa2cf 0%,#9fb5cc 40%,#8f8a84 100%)"></div>
    <div class="spec-label">GENERAL LABOR<span class="go"><svg width="10" height="8" viewBox="0 0 10 8"><path d="M1 4h8M6 1l3 3-3 3" fill="none" stroke="#fff"/></svg></span></div></div>
</section>

<h2 class="section-title" style="left:0;width:1200px;text-align:center;top:1693px;font-size:36px">Client Testimonials</h2>
<div class="slide-arrow" style="left:67px;top:1884px"><svg width="12" height="10" viewBox="0 0 12 10"><path d="M11 5H1M5 1L1 5l4 4" fill="none" stroke="#b5111f" stroke-width="1.4"/></svg></div>
<div class="slide-arrow" style="left:1100px;top:1884px"><svg width="12" height="10" viewBox="0 0 12 10"><path d="M1 5h10M7 1l4 4-4 4" fill="none" stroke="#b5111f" stroke-width="1.4"/></svg></div>
<article class="testimonial" style="left:122px">
  <span class="quote-mark">“</span>
  <p class="t-copy">Halvard Staffing Solutions helped us fill 25 roles in under 30 days. Their ability to scale and maintain quality is unmatched. Halvard Staffing Solutions helped us fill 25 roles in under 30 days. Their ability to scale and maintain quality is unmatched.”</p>
  <div class="avatar" role="img" aria-label="Client portrait"></div>
  <div class="stars">★★★★★</div>
  <div class="role">HR Director, Global IT Firm</div>
</article>
<article class="testimonial" style="left:609px">
  <span class="quote-mark">“</span>
  <p class="t-copy">We struggled to find specialized IT talent until we partnered with Halvard. Their recruitment team delivered top-tier candidates who hit the ground running. We struggled to find specialized IT talent until we partnered with Halvard.</p>
  <div class="avatar" role="img" aria-label="Client portrait"></div>
  <div class="stars">★★★★★</div>
  <div class="role">VP of Technology, FinTech Startup</div>
</article>

<section class="resources">
  <h2 class="section-title" style="left:122px;top:53px;font-size:35px">Resources</h2>
  <a class="btn-navy" style="left:946px;top:65px;width:131px;height:31px">View all Resources</a>
  <div class="slide-arrow" style="left:67px;top:235px"><svg width="12" height="10" viewBox="0 0 12 10"><path d="M11 5H1M5 1L1 5l4 4" fill="none" stroke="#b5111f" stroke-width="1.4"/></svg></div>
  <div class="slide-arrow" style="left:1100px;top:235px"><svg width="12" height="10" viewBox="0 0 12 10"><path d="M1 5h10M7 1l4 4-4 4" fill="none" stroke="#b5111f" stroke-width="1.4"/></svg></div>
  <div class="res-card" style="left:122px">
    <div class="res-img"><div class="photo" role="img" aria-label="Team meeting around a white table with laptops" style="background:radial-gradient(ellipse 110px 60px at 55% 65%,rgba(250,250,250,.95),rgba(250,250,250,0)),linear-gradient(180deg,#d9dadc 0%,#b7b9bd 35%,#6e737a 75%,#3f444b 100%)"></div></div>
    <h3 class="res-title">Top 5 Mistakes Companies Make When Hiring – And How to Avoid Them</h3>
    <a class="read-more">Read More <svg width="10" height="8" viewBox="0 0 10 8"><path d="M1 4h8M6 1l3 3-3 3" fill="none" stroke="#b5111f"/></svg></a>
  </div>
  <div class="res-card" style="left:447px">
    <div class="res-img"><div class="photo" role="img" aria-label="Colleagues working together on laptops in an office" style="background:radial-gradient(ellipse 100px 50px at 50% 78%,rgba(200,204,208,.9),rgba(200,204,208,0)),linear-gradient(180deg,#8fae93 0%,#7b8d86 30%,#3f4c5e 65%,#2a3140 100%)"></div></div>
    <h3 class="res-title">Scaling Fast? Why On-Demand Talent Could Be Your Secret Weapon</h3>
    <a class="read-more">Read More <svg width="10" height="8" viewBox="0 0 10 8"><path d="M1 4h8M6 1l3 3-3 3" fill="none" stroke="#b5111f"/></svg></a>
  </div>
  <div class="res-card" style="left:772px">
    <div class="res-img"><div class="photo" role="img" aria-label="Business team in suits giving thumbs up" style="background:radial-gradient(ellipse 150px 40px at 50% 38%,rgba(196,150,120,.55),rgba(196,150,120,0)),linear-gradient(180deg,#f2f2f2 0%,#e6e6e6 22%,#4a4d55 55%,#1e2026 100%)"></div></div>
    <h3 class="res-title">How to Spot High-Quality Candidates in a Crowded Talent Pool</h3>
    <a class="read-more">Read More <svg width="10" height="8" viewBox="0 0 10 8"><path d="M1 4h8M6 1l3 3-3 3" fill="none" stroke="#b5111f"/></svg></a>
  </div>
</section>

<h2 class="section-title" style="left:122px;top:2636px;font-size:23px;font-weight:400">Certifications Display</h2>
<a class="btn-navy" style="left:953px;top:2639px;width:124px;height:33px">Download Now</a>
<div class="badge-box" style="left:122px" aria-label="VOSB certification"><svg width="84" height="84"><circle cx="42" cy="42" r="40" fill="none" stroke="#2f4aa8" stroke-width="3"/></svg></div>
<div class="badge-box" style="left:381px" aria-label="Minority-Owned Business certification"><svg width="84" height="84"><circle cx="42" cy="42" r="40" fill="none" stroke="#6e7a73" stroke-width="3"/></svg></div>
<div class="badge-box" style="left:640px" aria-label="SDVOSB certification"><svg width="84" height="84"><circle cx="42" cy="42" r="40" fill="none" stroke="#2f4aa8" stroke-width="3"/></svg></div>
<div class="badge-box" style="left:900px" aria-label="DBE certification"><svg width="84" height="84"><circle cx="42" cy="42" r="40" fill="none" stroke="#1b1b1b" stroke-width="3"/></svg></div>

<section class="cta">
  <h2>NEED TALENT? WE DELIVER.</h2>
  <a class="btn">Get Started Now</a>
</section>

<footer class="site-footer">
  <div class="brand" style="top:60px;font-size:24px">HALVARD</div>
  <div class="f-title" style="left:122px;top:120px">Follow Us</div>
  <a class="social" style="left:122px" aria-label="Mingleo"></a>
  <a class="social" style="left:161px" aria-label="Profilary"></a>
  <a class="social" style="left:200px" aria-label="Quillo"></a>

  <div class="f-title" style="left:411px;top:60px">Quick Links</div>
  <a class="f-link" style="top:100px">Home</a>
  <a class="f-link" style="top:127px">About Us</a>
  <a class="f-link" style="top:154px">Solutions</a>
  <a class="f-link" style="top:181px">Resources</a>
  <a class="f-link" style="top:208px">Careers</a>

  <div class="f-title" style="left:603px;top:60px">Contact Info</div>
  <div class="contact" style="top:99px"><span class="ico"><svg width="9" height="9" viewBox="0 0 10 10"><path d="M2 1l2 2-1 1.5c.8 1.5 1.5 2.2 3 3L7.5 6 9.5 8 8 9.5C4 9 1 6 .5 2z" fill="none" stroke="#d8121f" stroke-width=".9"/></svg></span>+ 555-014-2870</div>
  <div class="contact" style="top:124px"><span class="ico"><svg width="10" height="8" viewBox="0 0 10 8"><rect x=".5" y=".5" width="9" height="7" fill="none" stroke="#d8121f"/><path d="M.5 .5l4.5 4 4.5-4" fill="none" stroke="#d8121f"/></svg></span>halvardstaffingsolutions<br>@.com</div>
  <div class="contact" style="top:165px"><span class="ico"><svg width="9" height="9" viewBox="0 0 10 10"><circle cx="5" cy="5" r="4.2" fill="none" stroke="#d8121f"/><path d="M1 5h8M5 1c-2 2.5-2 5.5 0 8M5 1c2 2.5 2 5.5 0 8" fill="none" stroke="#d8121f" stroke-width=".7"/></svg></span>halvardstaffing.example</div>

  <div class="f-title" style="left:866px;top:60px">Newsletter Signup</div>
  <div class="f-input">Email</div>
  <a class="f-sub">SUBSCRIBE</a>

  <div class="f-rule"></div>
  <p class="f-legal" style="left:122px">Copyright © 2025 Halvardstaffingsolutions All rights reserved.</p>
  <p class="f-legal" style="left:826px;word-spacing:2px">Company &nbsp;&nbsp; Privacy Policy &nbsp;&nbsp; Terms and Conditions</p>
</footer>

</body>
</html>
```